Web site for Physical Therapy Clinic

Looking for a web designer who has experience in planning & designing graphic user interfaces for web site.
You will be delivered a sitemap/flow diagram and a general visual concept and expected to deliver finished web GUI design in PSD (or any suitable) format.
RESPONSIBILITIES:
-Interpreting the sitemap/flow diagram into an user interface
-Developing a visual concept which aligns with the brands and project goals
-Building wireframes
-Design usable, technically feasible, great looking user interfaces in Photoshop(or Illustrator)
-Present your design in jpg format
-Delivering pixel perfect design ready to be converted to html/css
EXPECTATIONS:
-Adobe Creative Suite
-Deliver quality design by applying sound design practices with solid methodology, workflow & discipline.
-Manage the design process from start to finish, including gathering requirements and delivering final assets
-Strong sense of design and knowledge of typography, grid systems, color theory, usability, interactivity and information architecture principles
-Familiar with HTML, CSS, and JavaScript knowledge for optimizing design concepts around these technologies
-Familiar with standards-based, cross-browser, multi-device design
-Familiar with responsive web design/development
-Participate in estimating project efforts and delivery timelines
-Identify technical, schedule, and other project risks and provide relevant feedback
-Proactively collaborate and communicate
-Ability to multitask and prioritize multiple concurrent assignments
-High attention to detail
Corvela Physical Therapy provides personalized and high-quality therapy services. Patients are treated in two different settings; at our outpatient clinic or through home health visits. The services we provide are: Physical Therapy, Occupational Therapy, Speech Therapy and Massage Therapy.
We are looking for a designer/developer to build a fully-functional website for our business. The website needs to be:
• Fast-loading
• Mobile-compatible
• User-friendly
The following web address has been secured through namebarrow.example:
www.corvelapt.example
Tabs for the website will include...
Home
About
• History
• Team
Patients
• Services
• Insurances & payments accepted
• Coverage areas
Agencies
• Inquiries
• Forms & credentials
• Coverage areas
Therapists
• Reasons to work with us
• Career opportunities
• Application
FAQ
Contact
• Inquiries
• Locations
Breakdown of content needed on each page:
HOME
• Tagline
ABOUT
• History
• Team
PATIENTS
• Pain Management
- Neck & back pain
- Radiculopathy
- Sacroiliac Joint Syndrome
- Status Post Laminectomy
- Status Post Spinal Fusion
- Patellafemoral pain
- Arthritis: Osteoarthritis & Rheumatoid Arthritis
- Temporomandibular Joint
- Post-amputation
• Neurological Disorders
- Cerebral Vascular Accidents
- Parkinson's disease
- Multiple Sclerosis
- Traumatic & non-traumatic Brain Injury
- Spinal cord injury
- Guillain Barre
- Intracranial hemorrhage
- Diabetic neuropathy
- Post Polio Syndrome
• Work/Sport Injuries
- Carpal Tunnel Syndrome
- Disc Hernia
- Plantar Fasciitis
- Sciatica
- Frozen Shoulder
- Rotator Cuff injury/surgery
- Hip surgery
- Knee surgery: Anterior/Posterior Cruciate Ligament & Meniscal Tear
- Ankle sprain
- Tennis Elbow
- Golfer's Elbow
• Services
- Outpatient
- Home Health (with coverage area maps)
• Languages
- English
- Spanish
- Vietnamese
- Farsi
- Mandarin
- Tagalog
• Insurances Accepted
- HMO
- PPO
- Medicare
- Workers Compensation
• Physician Referral Form (printable PDF)
• Patient Registration Form (able to sign and print)
AGENCIES
• Physical Therapy Coverage Areas with map
• Occupational Therapy Coverage Areas with map
• Speech Therapy Coverage Areas with map
• Inquiry Form that goes directly to Corvela email
- Name
- Title
- Company
- Phone Number
- Email
- Question
• Password access to Credentials & Contact List (editable)
THERAPISTS
• Reasons to work with us
- check example (http://www.ostrandrehab.example/#!therapists/c10my)
- add Referral Bonus
• Career Opportunities editable through an excel worksheet
• Application form that goes directly to Corvela email
- check example (http://www.ostrandrehab.example/#!therapist-application-/cp7d)
FAQ
CONTACT
• Inquiry form
- option of "Agency" or "Patient"
- option of "Home Health Services" or "Outpatient Clinic"
- Question
• Clinic Location & Hours
30587 Marlowe Ave., Suite F
Garden Grove, CA 92843
Monday - Friday 8am - 5pm
• Home Health Office Hours
Monday - Friday 8:30am - 5:30pm
• Connect to social networks
- Linkedin
https://www.linkedin.com/profile/view?id=517093648&authType=NAME_SEARCH&authToken=qmRt&locale=en_US&trk=tyah&trkInfo=tarId%3A1598304716025%2Ctas%3Acorvela%20physical%20%2Cidx%3A1-1-1
- Facebook
https://www.facebook.com/pages/Corvela-Physical-Therapy/580917264315
Target Market(s)
Adult patients ages 18 to 80 in need of pain management and/or rehab. Home health agencies that contract therapists.
Industry/Entity Type
Architecture
Look and feel

```html
<!DOCTYPE html>
<html lang="en">
<head>
<meta charset="utf-8">
<title>Corvela Physical Therapy</title>
<link rel="stylesheet" href="https://fonts.googleapis.com/css2?family=Roboto:wght@300;400&family=Open+Sans:wght@400&family=Roboto+Slab:wght@400&display=swap">
<style>
:root{
  --brand-blue:#1e9be8;
  --band-blue:#21a1f1;
  --accent-red:#f2493a;
  --rule-grey:#e6e6e6;
  --card-border:#dcdcdc;
  --text-dark:#444;
  --icon-grey:#b5b5b5;
  --footer-bg:#303030;
  --footer-base:#2a2a2a;
  --footer-text:#a9a9a9;
  --footer-link:#e2e2e2;
  --footer-accent:#27b5d8;
  --field-border:#4a4a4a;
  --white:#fff;
}
*{box-sizing:border-box;margin:0;padding:0}
html,body{width:1107px;height:1200px;overflow:hidden;background:var(--white)}
body{position:relative;font-family:"Open Sans",Arial,sans-serif;color:var(--text-dark)}
.abs{position:absolute}

/* Team */
.team{position:absolute;left:0;top:0;width:1107px;height:413px;background:var(--white)}
.section-title{position:absolute;left:25px;top:17px;font:400 22px/26px "Roboto",Arial,sans-serif;color:var(--brand-blue);letter-spacing:.3px}
.title-rule{position:absolute;left:24px;top:52px;width:1026px;height:1px;background:var(--rule-grey)}
.title-accent{position:absolute;left:24px;top:50px;width:198px;height:4px;background:var(--accent-red)}
.card{position:absolute;top:86px;width:225px;height:284px;border:1px solid var(--card-border);background:var(--white)}
.card-photo{height:179px;margin:-1px -1px 0;background:linear-gradient(135deg,#eef0ee 0%,#d9c3a6 38%,#c79a66 55%,#f1ece6 75%,#dfe4e2 100%)}
.card-name{position:absolute;left:16px;top:190px;font:400 14px/18px "Open Sans",Arial,sans-serif;color:#4a4a4a;text-transform:uppercase}
.card-role{position:absolute;left:16px;top:214px;font:400 12px/16px "Open Sans",Arial,sans-serif;color:var(--brand-blue)}
.card-social{position:absolute;left:0;right:0;top:246px;height:37px;border-top:1px solid var(--card-border);display:flex;align-items:center;padding-left:17px;gap:22px}
.card-social span{width:13px;height:13px;border-radius:50%;background:var(--icon-grey)}

/* Testimonial */
.testimonials{position:absolute;left:0;top:413px;width:1107px;height:320px;background:var(--band-blue)}
.testimonials .section-title{left:30px;top:36px;font-size:20px;color:var(--white)}
.testimonials .title-rule{left:24px;top:71px;width:1018px;background:rgba(255,255,255,.85)}
.testimonials .title-accent{left:24px;top:71px;width:197px}
.patient-photo{position:absolute;left:81px;top:117px;width:157px;height:157px;border-radius:50%;border:3px solid var(--white);background:radial-gradient(circle at 50% 45%,#e9b89a 0%,#b0553a 45%,#6a2b1e 75%,#3f5b86 100%)}
.quote{position:absolute;left:288px;top:143px;width:690px;font:400 13px/20px "Open Sans",Arial,sans-serif;color:var(--white)}
.quote-rule{position:absolute;left:288px;top:232px;width:683px;border-top:1px dashed rgba(255,255,255,.8)}
.quote-author{position:absolute;left:287px;top:253px;font:400 16px/22px "Roboto Slab",Georgia,serif;color:var(--white)}
.slider-arrow{position:absolute;top:196px;width:16px;height:24px}

/* Footer */
.footer{position:absolute;left:0;top:733px;width:1107px;height:394px;background:var(--footer-bg)}
.col{position:absolute;top:36px}
.col-title{font:300 17px/22px "Roboto",Arial,sans-serif;color:var(--white)}
.col-rule{width:40px;height:2px;background:var(--footer-accent);margin-top:11px}
.about-text{position:absolute;left:27px;top:111px;width:222px;font:400 12px/16px "Roboto",Arial,sans-serif;color:var(--footer-text)}
.contact-line{position:absolute;left:56px;font:400 12px/16px "Roboto",Arial,sans-serif;color:var(--footer-text)}
.contact-line.light{color:var(--footer-link)}
.contact-line.accent{color:var(--footer-accent)}
.contact-icon{position:absolute;left:28px}
.link-list{position:absolute;top:113px;list-style:none}
.link-list li{position:relative;padding-left:16px;height:31px;font:400 12px/16px "Roboto",Arial,sans-serif;color:var(--footer-link)}
.link-list li::before{content:"";position:absolute;left:2px;top:5px;border-left:4px solid #777;border-top:3px solid transparent;border-bottom:3px solid transparent}
.field-label{position:absolute;left:792px;font:400 12px/16px "Roboto",Arial,sans-serif;color:var(--footer-text)}
.field-label em{font-style:normal;color:var(--footer-accent)}
.field{position:absolute;left:792px;width:224px;border:1px solid var(--field-border);background:var(--footer-bg)}
.submit{position:absolute;left:792px;top:317px;width:78px;height:34px;background:var(--white);color:#333;font:400 12px/34px "Roboto",Arial,sans-serif;text-align:center}
.base-bar{position:absolute;left:0;top:1127px;width:1107px;height:73px;background:var(--footer-base)}
.copyright{position:absolute;left:26px;top:25px;font:400 11px/16px "Roboto",Arial,sans-serif;color:var(--footer-link)}
.base-nav{position:absolute;right:69px;top:25px;display:flex;gap:9px;font:400 11px/16px "Roboto",Arial,sans-serif;color:var(--footer-link)}
</style>
</head>
<body>

<section class="team">
  <h2 class="section-title">OUR THERAPIST</h2>
  <div class="title-rule"></div>
  <div class="title-accent"></div>

  <article class="card" style="left:25px">
    <div class="card-photo" role="img" aria-label="Portrait of therapist Lena Marsh in a clinic"></div>
    <div class="card-name">Lena Marsh</div>
    <div class="card-role">lead Physio Therapist</div>
    <div class="card-social"><span></span><span></span><span></span><span></span></div>
  </article>
  <article class="card" style="left:288px">
    <div class="card-photo" role="img" aria-label="Portrait of therapist Lena Marsh in a clinic"></div>
    <div class="card-name">Lena Marsh</div>
    <div class="card-role">lead Physio Therapist</div>
    <div class="card-social"><span></span><span></span><span></span><span></span></div>
  </article>
  <article class="card" style="left:551px">
    <div class="card-photo" role="img" aria-label="Portrait of therapist Lena Marsh in a clinic"></div>
    <div class="card-name">Lena Marsh</div>
    <div class="card-role">lead Physio Therapist</div>
    <div class="card-social"><span></span><span></span><span></span><span></span></div>
  </article>
  <article class="card" style="left:814px">
    <div class="card-photo" role="img" aria-label="Portrait of therapist Lena Marsh in a clinic"></div>
    <div class="card-name">Lena Marsh</div>
    <div class="card-role">lead Physio Therapist</div>
    <div class="card-social"><span></span><span></span><span></span><span></span></div>
  </article>
</section>

<section class="testimonials">
  <h2 class="section-title">WHAT PATIENT SAYS ABOUT US?</h2>
  <div class="title-rule"></div>
  <div class="title-accent"></div>

  <svg class="slider-arrow" style="left:22px" viewBox="0 0 16 24" aria-hidden="true"><path d="M12 3 L4 12 L12 21" fill="none" stroke="#fff" stroke-width="3" stroke-linecap="round" stroke-linejoin="round"/></svg>
  <svg class="slider-arrow" style="left:1016px" viewBox="0 0 16 24" aria-hidden="true"><path d="M4 3 L12 12 L4 21" fill="none" stroke="#fff" stroke-width="3" stroke-linecap="round" stroke-linejoin="round"/></svg>

  <div class="patient-photo" role="img" aria-label="Portrait of patient Delia Fenwick"></div>
  <p class="quote">Thank you Tidy Harbor for making my house so fresh and clean! How nice it was to have all of my laundry washed and folded and my dishes done and put away along with everything else! Marta was so pleasant to have in my home. I have requested that she return next week! Oustanding you guys, keep it up!</p>
  <div class="quote-rule"></div>
  <div class="quote-author">Delia Fenwick, CEO of Quillby Company</div>
</section>

<footer class="footer">
  <div class="col" style="left:27px"><h3 class="col-title">Information</h3><div class="col-rule"></div></div>
  <div class="col" style="left:282px"><h3 class="col-title">Physiotherapist</h3><div class="col-rule"></div></div>
  <div class="col" style="left:548px"><h3 class="col-title">Services</h3><div class="col-rule"></div></div>
  <div class="col" style="left:788px"><h3 class="col-title">Quick Contact</h3><div class="col-rule"></div></div>

  <p class="about-text">Lorem Ipsum is simply dummy text of the printing and typesetting industry. Lorem Ipsum</p>

  <svg class="contact-icon" style="top:191px" width="13" height="16" viewBox="0 0 13 16" aria-hidden="true"><path d="M6.5 1a5 5 0 0 0-5 5c0 3.6 5 9 5 9s5-5.4 5-9a5 5 0 0 0-5-5z" fill="#27b5d8"/><circle cx="6.5" cy="6" r="2" fill="#303030"/></svg>
  <div class="contact-line" style="top:190px">Halvern Ltd.</div>
  <div class="contact-line" style="top:219px">27, Linden Ave<br>Riverton<br>NY</div>

  <svg class="contact-icon" style="top:281px;left:30px" width="10" height="16" viewBox="0 0 10 16" aria-hidden="true"><rect x="1" y="1" width="8" height="14" rx="1.5" fill="none" stroke="#27b5d8" stroke-width="1.6"/><rect x="4" y="12" width="2" height="1.2" fill="#27b5d8"/></svg>
  <svg class="abs" style="left:56px;top:283px" width="11" height="11" viewBox="0 0 11 11" aria-hidden="true"><circle cx="5.5" cy="5.5" r="5" fill="#27b5d8"/></svg>
  <div class="contact-line accent" style="top:281px;left:72px">(555) 014 27 93</div>

  <svg class="contact-icon" style="top:313px" width="15" height="11" viewBox="0 0 15 11" aria-hidden="true"><rect x="0" y="0" width="15" height="11" fill="#27b5d8"/><path d="M1 2 L7.5 6 L14 2" fill="none" stroke="#303030" stroke-width="1.3"/></svg>
  <div class="contact-line light" style="top:310px">info@halverndemo.example</div>

  <ul class="link-list" style="left:282px">
    <li>Dr. Lena Marsh</li>
    <li>Dr. Owen Pritchard</li>
    <li>Dr. Milo Brandt</li>
    <li>Dr. Ethan Rourke</li>
    <li>Dr. Felix Harlow</li>
    <li>Dr. Nora Ellwood</li>
    <li>Dr. Clara Voss</li>
  </ul>
  <ul class="link-list" style="left:550px">
    <li>Pediatric Clinic</li>
    <li>Diagnosis Clinic</li>
    <li>Cardiac Clinic</li>
    <li>Laboratory Analysis</li>
    <li>Dental Clinic</li>
    <li>Gynecological Clinic</li>
    <li>Psychological Counseling</li>
  </ul>

  <label class="field-label" style="top:111px">Your Email <em>*</em></label>
  <div class="field" style="top:137px;height:32px"></div>
  <label class="field-label" style="top:171px">Your message <em>*</em></label>
  <div class="field" style="top:196px;height:106px"></div>
  <div class="submit">Submit</div>
</footer>

<div class="base-bar">
  <div class="copyright">Corvela© 2014, All Rights Reserved</div>
  <nav class="base-nav"><span>Home</span><span>About</span><span>Physiotherapist</span><span>Services</span><span>FAQ</span><span>Contact</span></nav>
</div>

</body>
</html>
```